RKS Rovalin Kestra Sulvane company brochure

We need the design of brochure of a company that provides consultancy, design and supply of key equipment in the field of Wastewater, clean water, organic waste anaerobic treatment and green energy production for Industries. The attached files are:
RKS wording in english that describes activities
Some drawings (useful for design)
Presentation (in italian)
It would be nice to have a 4 pages brochure possibly in double language (english and italian).

Target Market(s)

water and waste

Industry/Entity Type

It Company

Colors

Designer to choose colors to be used in the design.

Requirements
Must have
• use the logo RKS as per attached docs

```html
<!DOCTYPE html>
<html lang="en">
<head>
<meta charset="utf-8">
<title>RKS Rovalin Kestra Sulvane – Brochure Spread</title>
<link href="https://fonts.googleapis.com/css2?family=Arimo:ital,wght@0,400;0,700;1,400;1,700&display=swap" rel="stylesheet">
<style>
  :root {
    --backdrop: #6b6b6b;
    --band: #525a70;
    --band-light: #5f6780;
    --rule: #d8dbe3;
    --paper-top: #ffffff;
    --paper-bottom: #e4e6ea;
    --ink: #2a2a2a;
    --white: #ffffff;
    --strip-gap: #f2f2f2;
  }
  * { box-sizing: border-box; margin: 0; padding: 0; }
  html, body { width: 1200px; height: 481px; overflow: hidden; background: var(--backdrop); }
  body { font-family: "Arimo", Arial, sans-serif; color: var(--ink); }
  .spread { display: flex; width: 1200px; height: 481px; }
  .page {
    position: relative; width: 600px; height: 481px;
    background: linear-gradient(180deg, var(--paper-top) 30%, var(--paper-bottom) 100%);
    display: flex; flex-direction: column;
  }
  .page--left { border-right: 1px solid #c9ccd2; }
  .page-header {
    height: 86px; background: linear-gradient(180deg, var(--band-light), var(--band));
    color: var(--white); text-align: center; padding-top: 12px;
  }
  .page-title { font-size: 24px; line-height: 30px; }
  .page-title--en { font-style: italic; font-weight: 400; }
  .page-title--en b { font-weight: 700; }
  .page-title--strong { font-weight: 700; font-style: normal; font-size: 21px; }
  .title-rule { width: 260px; height: 1px; background: var(--rule); margin: 3px auto 5px; }
  .page-subtitle { font-size: 18px; line-height: 22px; font-style: italic; }
  .page-subtitle b { font-weight: 700; }
  .page-subtitle--plain { font-style: normal; font-size: 20px; }
  .page-body { flex: 1; display: flex; gap: 22px; padding: 30px 30px 0 40px; }
  .page--right .page-body { padding: 14px 24px 0 22px; gap: 16px; }
  .column { flex: 1; font-size: 11.5px; line-height: 14px; }
  .column p { margin-bottom: 14px; }
  .column--lead { padding-top: 16px; }
  .tech-list { list-style: none; font-size: 10.5px; line-height: 13px; }
  .tech-list > li { margin-bottom: 14px; display: flex; }
  .tech-list .num { font-weight: 700; width: 22px; flex: none; font-size: 11.5px; }
  .tech-list ol { list-style: lower-alpha; padding-left: 24px; }
  .photo-strip { height: 96px; display: flex; gap: 3px; padding: 3px 0 0; background: var(--strip-gap); }
  .photo { flex: 1; }
  .photo--steel { background: linear-gradient(160deg, #b7bcc2, #6c7178); }
  .photo--pool { background: linear-gradient(180deg, #b8c9c8, #5fa7a8); }
  .photo--plant { background: linear-gradient(160deg, #a9a59a, #6f6b60); }
  .photo--sky { background: linear-gradient(180deg, #6d96c8, #c6cbd0 60%, #8a8d90); }
  .photo--basin { background: linear-gradient(180deg, #7e9270, #4b6a7a); }
  .photo--clarifier { background: linear-gradient(180deg, #b9bcb8, #7b7e7a); }
  .photo--tank { background: radial-gradient(circle at 50% 60%, #e6e6e2, #8c8a84); }
  .photo--sludge { background: linear-gradient(160deg, #d7c7a4, #a48a5a); }
  .photo--field { background: linear-gradient(180deg, #b4a796, #6f7458 70%, #5b6a78); }
  .photo--circular { background: linear-gradient(180deg, #9aa0a4, #6f8a90); }
</style>
</head>
<body>
<div class="spread">
  <section class="page page--left">
    <header class="page-header">
      <h1 class="page-title page-title--en"><b>Why</b> to chose us<b>?</b></h1>
      <div class="title-rule"></div>
      <h2 class="page-subtitle"><b>Perché</b> sceglierci<b>?</b></h2>
    </header>
    <div class="page-body">
      <div class="column column--lead">
        <p><b><i>Cost reduction</i></b><i>: WE first identifies the inefficient processes and remove them.</i></p>
        <p>Only when the emission reduction is not any more possible or economically feasible, WE propose the <b><i>best treatment</i></b> to the client.</p>
        <p><i>WE provide best solutions on a variety of </i><b><i>biological and chemical processes</i></b>.</p>
        <p><i>WE provide highly qualified and </i><b><i>indipended consultancy.</i></b></p>
      </div>
      <div class="column">
        <p>Riduzione dei costi: prima identifichiamo i processi inefficienti e li rimuoviamo.</p>
        <p>Solo quando la riduzione delle emissioni non è più possibile o economicamente fattibile, proponiamo il miglior trattamento al cliente.</p>
        <p>Forniamo le migliori soluzioni su una varietà di processi biologici e chimici.</p>
        <p>Offriamo consulenza altamente qualificata e indipendente.</p>
      </div>
    </div>
    <div class="photo-strip">
      <div class="photo photo--steel" role="img" aria-label="Photo of stainless steel treatment units"></div>
      <div class="photo photo--pool" role="img" aria-label="Photo of an aeration basin with water"></div>
      <div class="photo photo--plant" role="img" aria-label="Photo of an industrial treatment plant"></div>
      <div class="photo photo--sky" role="img" aria-label="Photo of process piping and tanks under blue sky"></div>
      <div class="photo photo--basin" role="img" aria-label="Photo of an outdoor treatment basin"></div>
    </div>
  </section>

  <section class="page page--right">
    <header class="page-header">
      <h1 class="page-title page-title--strong">Proposed Technologies</h1>
      <div class="title-rule"></div>
      <h2 class="page-subtitle page-subtitle--plain">Tecnologie proposte</h2>
    </header>
    <div class="page-body">
      <ul class="column tech-list">
        <li><span class="num">1.</span><div>Biological processes:
          <ol><li>Oxidation, nitrification, denitrification, P-removal</li><li>N-recovery and slow release fertilizers production</li><li>Anaerobic processes</li><li>Metal recovery</li></ol></div></li>
        <li><span class="num">2.</span><div>High value products recovery</div></li>
        <li><span class="num">3.</span><div>Chemico/Phisical processes:
          <ol><li>Flottation</li><li>Filtration and membrane filtration</li><li>Chemical oxidations / reductions (e.g. Fenton, colour removal, CN, Cr6+ removal)</li><li>Disinfection</li></ol></div></li>
        <li><span class="num">4.</span><div>Water recovery and recycle</div></li>
      </ul>
      <ul class="column tech-list">
        <li><span class="num">1.</span><div>Processi biologici:
          <ol><li>Ossidazione, nitrificazione, denitrificazione, P-rimozione</li><li>Fertilizzanti N-recovery e a rilascio lento produzione</li><li>Processi anaerobici</li><li>Recupero di metalli</li></ol></div></li>
        <li><span class="num">2.</span><div>Recupero di prodotti di alto valore</div></li>
        <li><span class="num">3.</span><div>Processi chimico / fisici:
          <ol><li>Flottazione</li><li>Filtrazione e filtrazione a membrana</li><li>Ossidazioni / riduzioni chimiche (ad es. Fenton, rimozione del colore, CN, rimozione Cr6 +)</li><li>Disinfezione</li></ol></div></li>
        <li><span class="num">4.</span><div>Recupero e riciclaggio dell'acqua</div></li>
      </ul>
    </div>
    <div class="photo-strip">
      <div class="photo photo--clarifier" role="img" aria-label="Photo of a circular clarifier tank"></div>
      <div class="photo photo--tank" role="img" aria-label="Photo of a flotation tank seen from above"></div>
      <div class="photo photo--sludge" role="img" aria-label="Photo of a sludge treatment unit"></div>
      <div class="photo photo--field" role="img" aria-label="Photo of a treatment plant in the countryside"></div>
      <div class="photo photo--circular" role="img" aria-label="Photo of a round settling basin"></div>
    </div>
  </section>
</div>
</body>
</html>
```